Business card and stationery for VIP parking
Velmor Bay s.r.o.
I need double sided standard sized Business Card [3.5" x 2"]
Please, be creatives
Professional
Milan Vesecky
CEO
Na Lukách 512/27, Prague
Czech Republic 164 00
milan.vesecky@velmorbay.cz
www.velmorbay.cz
The business card should be very creative, professional, using the logo's color combinations. I also need envelopes, folders and all stationery set.
Some picture.

```html
<!DOCTYPE html>
<html lang="en">
<head>
<meta charset="utf-8">
<title>Velmor Bay s.r.o. – Stationery Set</title>
<link href="https://fonts.googleapis.com/css2?family=Open+Sans:wght@400;700&display=swap" rel="stylesheet">
<style>
  :root{
    --red:#d5232b;
    --red-dark:#a8161d;
    --blue:#1d4f9f;
    --blue-dark:#123677;
    --paper:#ffffff;
    --ink:#3a3a3a;
    --stage:#e9e9ea;
  }
  *{box-sizing:border-box;margin:0;padding:0}
  html,body{width:1200px;height:499px;overflow:hidden;background:var(--stage);font-family:"Open Sans",Arial,sans-serif;color:var(--ink)}
  .set{position:absolute;left:0;width:1200px;height:249px}
  .set--red{top:0;--accent:var(--red);--accent-dark:var(--red-dark);--second:var(--blue)}
  .set--blue{top:250px;--accent:var(--blue);--accent-dark:var(--blue-dark);--second:var(--red)}
  .sheet{position:absolute;background:var(--paper);box-shadow:0 1px 4px rgba(0,0,0,.25);overflow:hidden}

  .brand{display:flex;align-items:center;gap:4px;font-weight:700;color:var(--red);white-space:nowrap;line-height:1}
  .brand__mark{background:var(--blue);flex:none}
  .brand--light{color:#fff}
  .brand--light .brand__mark{background:#fff}

  .watermark{position:absolute;background:currentColor;opacity:.08;border-radius:6px}
  .wave{position:absolute;left:0;bottom:0;width:100%}

  /* cards */
  .card{width:88px;height:50px;left:24px}
  .card .brand{position:absolute;left:12px;top:18px;font-size:9px}
  .card .brand__mark{width:8px;height:8px}
  .card--accent{background:var(--accent)}
  .card__lines{position:absolute;left:8px;bottom:8px;font-size:3.5px;line-height:1.5}
  .card__name{font-weight:700;font-size:5px;color:var(--accent)}

  /* letterhead */
  .letterhead{top:24px;width:140px;height:214px}
  .letterhead .brand{position:absolute;right:10px;top:12px;font-size:9px}
  .letterhead .brand__mark{width:8px;height:8px}
  .letterhead .watermark{left:18px;top:50px;width:80px;height:80px;color:var(--accent)}
  .letterhead__foot{position:absolute;left:10px;bottom:22px;font-size:3.5px;line-height:1.5}

  /* folders */
  .folder{top:24px;height:216px}
  .folder--cover{background:var(--accent)}
  .folder--cover .watermark{color:#fff;opacity:.12;width:110px;height:110px;left:10px;top:14px}
  .folder__inside .brand{position:absolute;left:50%;top:92px;transform:translateX(-50%);font-size:14px}
  .folder__inside .brand__mark{width:12px;height:12px}
  .folder__foot{position:absolute;left:12px;bottom:30px;font-size:3.5px;line-height:1.5}

  /* envelopes */
  .envelope{left:1068px;width:120px;height:50px}
  .envelope .brand{position:absolute;left:10px;top:8px;font-size:8px}
  .envelope .brand__mark{width:7px;height:7px}
</style>
</head>
<body>

<section class="set set--red" aria-label="Red stationery set">
  <div class="sheet card" style="top:24px">
    <div class="brand"><span class="brand__mark"></span>Velmor Bay</div>
  </div>
  <div class="sheet card" style="top:80px">
    <div class="card__lines"><div class="card__name">Milan Vesecky</div>CEO<br>Na Lukách 512/27, Prague 164 00<br>milan.vesecky@velmorbay.cz</div>
  </div>
  <div class="sheet card card--accent" style="top:136px">
    <div class="brand brand--light"><span class="brand__mark"></span>Velmor Bay</div>
  </div>
  <div class="sheet card" style="top:192px;background:var(--second)">
    <div class="brand brand--light"><span class="brand__mark"></span>Velmor Bay</div>
  </div>

  <div class="sheet letterhead" style="left:125px">
    <div class="watermark"></div>
    <div class="brand"><span class="brand__mark"></span>Velmor Bay</div>
    <div class="letterhead__foot">Na Lukách 512/27, Prague 164 00<br>milan.vesecky@velmorbay.cz<br>www.velmorbay.cz</div>
    <svg class="wave" viewBox="0 0 140 20" height="20" preserveAspectRatio="none"><path d="M0 12 Q70 0 140 10 V20 H0Z" fill="var(--second)"/><path d="M0 16 Q70 6 140 14 V20 H0Z" fill="var(--accent)"/></svg>
  </div>
  <div class="sheet letterhead" style="left:278px">
    <div class="watermark"></div>
    <div class="brand"><span class="brand__mark"></span>Velmor Bay</div>
    <div class="letterhead__foot">Na Lukách 512/27, Prague 164 00<br>milan.vesecky@velmorbay.cz<br>www.velmorbay.cz</div>
    <svg class="wave" viewBox="0 0 140 20" height="20" preserveAspectRatio="none"><path d="M0 12 Q70 0 140 10 V20 H0Z" fill="var(--second)"/><path d="M0 16 Q70 6 140 14 V20 H0Z" fill="var(--accent)"/></svg>
  </div>

  <div class="sheet folder folder--cover" style="left:432px;width:161px"><div class="watermark"></div></div>
  <div class="sheet folder folder__inside" style="left:593px;width:151px">
    <div class="brand"><span class="brand__mark"></span>Velmor Bay</div>
    <div class="folder__foot">Na Lukách 512/27, Prague<br>www.velmorbay.cz</div>
    <svg class="wave" viewBox="0 0 150 22" height="22" preserveAspectRatio="none"><path d="M0 14 Q75 0 150 12 V22 H0Z" fill="var(--second)"/><path d="M0 18 Q75 6 150 16 V22 H0Z" fill="var(--accent)"/></svg>
  </div>

  <div class="sheet folder folder__inside" style="left:754px;width:302px">
    <svg style="position:absolute;left:0;top:0" width="150" height="216" viewBox="0 0 150 216" preserveAspectRatio="none"><path d="M0 0 H140 Q120 108 145 216 H0Z" fill="var(--accent)"/></svg>
    <div class="watermark" style="color:#fff;opacity:.12;width:100px;height:100px;left:10px;top:14px"></div>
    <div class="brand" style="left:226px"><span class="brand__mark"></span>Velmor Bay</div>
  </div>

  <div class="sheet envelope" style="top:36px">
    <div class="brand"><span class="brand__mark"></span>Velmor Bay</div>
    <svg class="wave" viewBox="0 0 120 10" height="10" preserveAspectRatio="none"><path d="M0 5 Q60 0 120 4 V10 H0Z" fill="var(--second)"/><path d="M0 8 Q60 3 120 7 V10 H0Z" fill="var(--accent)"/></svg>
  </div>
  <div class="sheet envelope" style="top:106px">
    <div class="brand"><span class="brand__mark"></span>Velmor Bay</div>
    <svg class="wave" viewBox="0 0 120 10" height="10" preserveAspectRatio="none"><path d="M0 5 Q60 0 120 4 V10 H0Z" fill="var(--second)"/><path d="M0 8 Q60 3 120 7 V10 H0Z" fill="var(--accent)"/></svg>
  </div>
</section>

<section class="set set--blue" aria-label="Blue stationery set">
  <div class="sheet card" style="top:14px">
    <div class="brand"><span class="brand__mark"></span>Velmor Bay</div>
  </div>
  <div class="sheet card" style="top:70px">
    <div class="card__lines"><div class="card__name">Milan Vesecky</div>CEO<br>Na Lukách 512/27, Prague 164 00<br>milan.vesecky@velmorbay.cz</div>
  </div>
  <div class="sheet card" style="top:126px;background:var(--second)">
    <div class="brand brand--light"><span class="brand__mark"></span>Velmor Bay</div>
  </div>
  <div class="sheet card card--accent" style="top:182px">
    <div class="brand brand--light"><span class="brand__mark"></span>Velmor Bay</div>
  </div>

  <div class="sheet letterhead" style="left:125px">
    <div class="watermark"></div>
    <div class="brand"><span class="brand__mark"></span>Velmor Bay</div>
    <div class="letterhead__foot">Na Lukách 512/27, Prague 164 00<br>milan.vesecky@velmorbay.cz<br>www.velmorbay.cz</div>
    <svg class="wave" viewBox="0 0 140 20" height="20" preserveAspectRatio="none"><path d="M0 12 Q70 0 140 10 V20 H0Z" fill="var(--second)"/><path d="M0 16 Q70 6 140 14 V20 H0Z" fill="var(--accent)"/></svg>
  </div>
  <div class="sheet letterhead" style="left:278px">
    <div class="watermark"></div>
    <div class="brand"><span class="brand__mark"></span>Velmor Bay</div>
    <div class="letterhead__foot">Na Lukách 512/27, Prague 164 00<br>milan.vesecky@velmorbay.cz<br>www.velmorbay.cz</div>
    <svg class="wave" viewBox="0 0 140 20" height="20" preserveAspectRatio="none"><path d="M0 12 Q70 0 140 10 V20 H0Z" fill="var(--second)"/><path d="M0 16 Q70 6 140 14 V20 H0Z" fill="var(--accent)"/></svg>
  </div>

  <div class="sheet folder folder--cover" style="left:432px;width:161px"><div class="watermark"></div></div>
  <div class="sheet folder folder__inside" style="left:593px;width:151px">
    <div class="brand"><span class="brand__mark"></span>Velmor Bay</div>
    <div class="folder__foot">Na Lukách 512/27, Prague<br>www.velmorbay.cz</div>
    <svg class="wave" viewBox="0 0 150 22" height="22" preserveAspectRatio="none"><path d="M0 14 Q75 0 150 12 V22 H0Z" fill="var(--second)"/><path d="M0 18 Q75 6 150 16 V22 H0Z" fill="var(--accent)"/></svg>
  </div>

  <div class="sheet folder folder__inside" style="left:754px;width:302px">
    <svg style="position:absolute;left:0;top:0" width="150" height="216" viewBox="0 0 150 216" preserveAspectRatio="none"><path d="M0 0 H140 Q120 108 145 216 H0Z" fill="var(--accent)"/></svg>
    <div class="watermark" style="color:#fff;opacity:.12;width:100px;height:100px;left:10px;top:14px"></div>
    <div class="brand" style="left:226px"><span class="brand__mark"></span>Velmor Bay</div>
  </div>

  <div class="sheet envelope" style="top:36px">
    <div class="brand"><span class="brand__mark"></span>Velmor Bay</div>
    <svg class="wave" viewBox="0 0 120 10" height="10" preserveAspectRatio="none"><path d="M0 5 Q60 0 120 4 V10 H0Z" fill="var(--second)"/><path d="M0 8 Q60 3 120 7 V10 H0Z" fill="var(--accent)"/></svg>
  </div>
  <div class="sheet envelope" style="top:106px">
    <div class="brand"><span class="brand__mark"></span>Velmor Bay</div>
    <svg class="wave" viewBox="0 0 120 10" height="10" preserveAspectRatio="none"><path d="M0 5 Q60 0 120 4 V10 H0Z" fill="var(--second)"/><path d="M0 8 Q60 3 120 7 V10 H0Z" fill="var(--accent)"/></svg>
  </div>
</section>

</body>
</html>
```